IT Company needs stationary design

Business cards, MS Word, PowerPoint, A4 notepad design base on our company logo. This must be a set of templates in the same style which could be used both for printable documents as well as for documents shared digitally via email, website etc. This should be a modern design which is still professional, so make sure content is well readable both in MS Word and MS PowerPoint templates.
Updates

Target Market(s)

SME and Corporate

Industry/Entity Type

It Company

Font styles to use
Sans Serif

Colors
0455a3
0692cd
f37122
ffc214

Requirements
Must have
• 1) Business cards design: modern but still professional
• 2) MS Word: mostly for IT project documents (business analysis, reports, specifications, etc.) must be professional and easy readable.
• 3) MS PowerPoint: first slide, normal slide, last slide.
• 4) A4 notepad: header (must), footer (must), some light design on the background (optionally)
Nice to have
• Business cards design: would be nice to have 2-4 color variations of the same design from one side - cover (for example part of the cards are blue, part of the cards are orange) and other side with contact details is identical.

```html
<!DOCTYPE html>
<html lang="en">
<head>
<meta charset="utf-8">
<title>Northvale business card</title>
<link href="https://fonts.googleapis.com/css2?family=Montserrat:wght@300;400;500;700&display=swap" rel="stylesheet">
<style>
  :root {
    --brand-navy: #0455a3;
    --brand-blue: #0692cd;
    --brand-orange: #f37122;
    --brand-yellow: #ffc214;
    --ink: #1c1c1c;
    --ink-soft: #4a4a4a;
    --card-white: #fbfbfb;
    --card-black: #0d0d0d;
    --backdrop: #ececec;
    --wordmark-light: #c9c9c9;
  }
  * { margin: 0; padding: 0; box-sizing: border-box; }
  html, body { width: 1200px; height: 763px; overflow: hidden; }
  body {
    background: var(--backdrop);
    font-family: "Montserrat", sans-serif;
    color: var(--ink);
  }
  .canvas {
    position: relative;
    width: 1200px;
    height: 763px;
  }
  .card {
    position: absolute;
    top: 245px;
    width: 480px;
    height: 274px;
    overflow: hidden;
    box-shadow: 0 6px 18px rgba(0,0,0,0.12);
  }
  /* Front: contact side */
  .card-front {
    left: 90px;
    background: var(--card-white);
  }
  .brand {
    position: absolute;
    left: 28px;
    top: 26px;
    display: flex;
    align-items: center;
    gap: 10px;
  }
  .brand-dot {
    width: 30px;
    height: 30px;
    border-radius: 50%;
    background: var(--brand-blue);
  }
  .brand-name {
    font-weight: 300;
    font-size: 26px;
    letter-spacing: 0.5px;
    color: var(--ink);
  }
  .person {
    position: absolute;
    left: 28px;
    top: 92px;
  }
  .person-name {
    font-weight: 700;
    font-size: 14px;
    letter-spacing: 1px;
    text-transform: uppercase;
  }
  .person-title {
    font-weight: 500;
    font-size: 10px;
    color: var(--brand-orange);
    margin-top: 3px;
  }
  .person-address {
    font-size: 9px;
    line-height: 1.45;
    color: var(--ink-soft);
    margin-top: 6px;
  }
  .contacts {
    position: absolute;
    left: 246px;
    top: 150px;
    padding-left: 16px;
    border-left: 1px solid #bdbdbd;
    list-style: none;
  }
  .contact-item {
    display: flex;
    align-items: center;
    gap: 8px;
    font-size: 9.5px;
    line-height: 1;
    height: 17px;
    color: var(--ink);
  }
  .contact-icon { width: 10px; height: 10px; flex: none; }
  .stripe {
    position: absolute;
    left: 0;
    right: 0;
    bottom: 0;
    height: 7px;
    display: flex;
  }
  .stripe-dark { flex: 0 0 222px; background: var(--ink); }
  .stripe-blue { flex: 0 0 128px; background: var(--brand-blue); }
  .stripe-orange { flex: 0 0 70px; background: var(--brand-orange); }
  .stripe-yellow { flex: 1; background: var(--brand-yellow); }

  /* Back: brand side */
  .card-back {
    left: 630px;
    background: var(--card-black);
    display: flex;
    flex-direction: column;
    align-items: center;
    justify-content: center;
    gap: 12px;
  }
  .card-back .brand-dot {
    width: 54px;
    height: 54px;
  }
  .card-back .brand-name {
    font-size: 28px;
    color: var(--wordmark-light);
  }
</style>
</head>
<body>
<main class="canvas">
  <section class="card card-front" aria-label="Business card, contact side">
    <div class="brand">
      <span class="brand-dot"></span>
      <span class="brand-name">northvale</span>
    </div>
    <div class="person">
      <p class="person-name">Daniel Reyes</p>
      <p class="person-title">Managing Partner</p>
      <p class="person-address">2870 Alder Lane, Suite 12<br>Riverton, CA 95410</p>
    </div>
    <ul class="contacts">
      <li class="contact-item">
        <svg class="contact-icon" viewBox="0 0 10 10"><rect x="2.5" y="0.5" width="5" height="9" rx="1" fill="var(--brand-orange)"/><rect x="3.5" y="1.8" width="3" height="5.5" fill="#fff"/></svg>
        (555) 218 4073
      </li>
      <li class="contact-item">
        <svg class="contact-icon" viewBox="0 0 10 10"><path d="M2 1 L4 1 L4.8 3.2 L3.6 4.2 Q4.6 6 6 6.6 L7 5.4 L9 6.2 L9 8.4 Q5 9 2.4 5.8 Q0.8 3.4 2 1 Z" fill="var(--brand-orange)"/></svg>
        (555) 309 6621
      </li>
      <li class="contact-item">
        <svg class="contact-icon" viewBox="0 0 10 10"><rect x="0.5" y="2" width="9" height="6" fill="none" stroke="var(--brand-orange)" stroke-width="1"/><path d="M0.5 2 L5 5.5 L9.5 2" fill="none" stroke="var(--brand-orange)" stroke-width="1"/></svg>
        hello@northvale.io
      </li>
      <li class="contact-item">
        <svg class="contact-icon" viewBox="0 0 10 10"><circle cx="5" cy="5" r="4.5" fill="var(--brand-orange)" opacity="0.55"/></svg>
        www.northvale.io
      </li>
    </ul>
    <div class="stripe" aria-hidden="true">
      <span class="stripe-dark"></span>
      <span class="stripe-blue"></span>
      <span class="stripe-orange"></span>
      <span class="stripe-yellow"></span>
    </div>
  </section>

  <section class="card card-back" aria-label="Business card, brand side">
    <span class="brand-dot"></span>
    <span class="brand-name">northvale</span>
  </section>
</main>
</body>
</html>
```